Business Card Design

I need a business card for company that is a limited company that was originally an off-road vehicle company (atv's side by sides snowmobiles and motorcycles) and I have recently sold the assets of the company that was operating under a different name and have become semi retired. I continue to do maintenance on these types of vehicles and also sell and install parts and accessories. Recently I have also contracted to a snowmobile club to operate their groomer to groom the snowmobile trails. I would like bright and bold colors.
Industry/Entity Type
Club
Contact Information for Business Card
KTV Holdings Ltd.
Milo Fenwick
780-413-2769

```html
<!DOCTYPE html>
<html lang="en">
<head>
<meta charset="utf-8">
<title>KTV Holdings Ltd. — Business Card</title>
<link rel="stylesheet" href="https://fonts.googleapis.com/css2?family=Saira+Condensed:wght@400;500;600;700&display=swap">
<style>
  :root {
    --navy: #17396a;
    --navy-deep: #15365f;
    --orange: #ec6f2d;
    --white: #ffffff;
    --ink-soft: #dfe6ef;
    --quote-mark: #6f86a6;
    --page: #f2f3f5;
  }
  * { box-sizing: border-box; margin: 0; padding: 0; }
  html, body {
    width: 1200px;
    height: 1200px;
    overflow: hidden;
    background: var(--page);
  }
  .sheet {
    width: 1200px;
    height: 1200px;
    display: flex;
    flex-direction: column;
    align-items: center;
    justify-content: center;
    gap: 60px;
    font-family: "Saira Condensed", sans-serif;
  }
  .card {
    position: relative;
    width: 900px;
    height: 514px;
    background: var(--navy);
    overflow: hidden;
    box-shadow: 0 6px 18px rgba(0, 0, 0, 0.18);
  }

  /* Front */
  .card-front .swoosh {
    position: absolute;
    inset: 0;
    width: 100%;
    height: 100%;
  }
  .company-name {
    position: absolute;
    top: 92px;
    right: 30px;
    font-weight: 600;
    font-size: 34px;
    line-height: 1;
    color: var(--white);
    white-space: nowrap;
  }
  .holder-name {
    position: absolute;
    top: 160px;
    left: 150px;
    font-weight: 600;
    font-size: 84px;
    line-height: 1;
    color: var(--white);
    letter-spacing: 1px;
  }
  .contact {
    position: absolute;
    top: 300px;
    left: 110px;
    display: flex;
    align-items: stretch;
    color: var(--ink-soft);
  }
  .contact-item {
    display: flex;
    flex-direction: column;
    align-items: center;
    gap: 20px;
    padding: 10px 36px;
    font-size: 26px;
    font-weight: 500;
    letter-spacing: 0.5px;
  }
  .contact-item svg { width: 34px; height: 34px; }
  .contact-item.email { padding-top: 40px; }
  .contact-divider {
    width: 2px;
    height: 150px;
    background: linear-gradient(to bottom, transparent, var(--ink-soft), transparent);
    transform: rotate(12deg);
    margin: 0 10px;
  }

  /* Back */
  .card-back { background: var(--navy-deep); }
  .quote-mark {
    position: absolute;
    font-weight: 700;
    font-size: 130px;
    line-height: 1;
    color: var(--quote-mark);
  }
  .quote-mark.open { top: 60px; left: 110px; }
  .quote-mark.close { top: 230px; right: 70px; }
  .statement {
    position: absolute;
    top: 120px;
    left: 180px;
    width: 640px;
    font-weight: 500;
    font-size: 24px;
    line-height: 1.5;
    letter-spacing: 0.6px;
    color: var(--ink-soft);
  }
</style>
</head>
<body>
<main class="sheet">

  <section class="card card-front" aria-label="Business card front">
    <svg class="swoosh" viewBox="0 0 900 514" preserveAspectRatio="none" aria-hidden="true">
      <path d="M30,0 C300,12 560,70 720,175 C800,228 860,280 900,330 L900,0 Z" fill="var(--orange)"/>
    </svg>
    <p class="company-name">KTV Holdings Ltd.</p>
    <h1 class="holder-name">Milo Fenwick</h1>
    <div class="contact">
      <div class="contact-item phone">
        <svg viewBox="0 0 24 24" aria-hidden="true">
          <path d="M6.6 3.5l2.6 3.2-1.6 2a12 12 0 0 0 5.7 5.7l2-1.6 3.2 2.6-1.5 2.6c-6.9-.4-12.1-5.6-12.5-12.5z" fill="none" stroke="var(--ink-soft)" stroke-width="1.5" stroke-linejoin="round"/>
        </svg>
        <span>780-413-2769</span>
      </div>
      <div class="contact-divider" aria-hidden="true"></div>
      <div class="contact-item email">
        <svg viewBox="0 0 24 24" aria-hidden="true">
          <rect x="2.5" y="5.5" width="19" height="13" fill="none" stroke="var(--ink-soft)" stroke-width="1.4"/>
          <path d="M2.5 5.5l9.5 7.5 9.5-7.5M2.5 18.5l7-6.5M21.5 18.5l-7-6.5" fill="none" stroke="var(--ink-soft)" stroke-width="1.4"/>
        </svg>
        <span>ktvhold.77@fenmail.ca</span>
      </div>
    </div>
  </section>

  <section class="card card-back" aria-label="Business card back">
    <span class="quote-mark open" aria-hidden="true">&ldquo;</span>
    <p class="statement">I am a journeyman red seal automotive technician journeyman red seal motorcycle technician and journeyman parts man.</p>
    <span class="quote-mark close" aria-hidden="true">&rdquo;</span>
  </section>

</main>
</body>
</html>
```